Bramblecourt Homes Stationary
Fast Settlements
Professional
Dorian Pelletier
Managing Member
4817 Larkspur Ave Suite 210
Washington, DC
dgpelletier@bramblecourthomes.net
www.bramblecourthomes.net
Business License # 782645113058
Cash Buyer, Fast Closing.
Residential and Commercial
We are a Nation Wide Buyer.
will upload ai file shortly
vector logo file

```html
<!DOCTYPE html>
<html lang="en">
<head>
<meta charset="utf-8">
<title>Bramblecourt Homes Stationary</title>
<link href="https://fonts.googleapis.com/css2?family=Montserrat:wght@400;500;700&display=swap" rel="stylesheet">
<style>
  :root {
    --backdrop: #e8e9eb;
    --paper: #ffffff;
    --paper-edge: #d9dadc;
    --brand-green: #1f9a4a;
    --brand-green-dark: #0f7434;
    --ghost-green: #e6f1ea;
    --ink: #3a3a3a;
    --ink-soft: #8a8a8a;
    --rule-dark: #1c1c1c;
  }
  * { box-sizing: border-box; margin: 0; padding: 0; }
  html, body { width: 1200px; height: 936px; overflow: hidden; }
  body {
    background: var(--backdrop);
    font-family: "Montserrat", Arial, sans-serif;
    color: var(--ink);
    position: relative;
  }
  .sheet {
    position: absolute;
    background: var(--paper);
    border: 1px solid var(--paper-edge);
    overflow: hidden;
    box-shadow: 0 2px 6px rgba(0,0,0,0.08);
  }
  .brand {
    display: flex;
    align-items: center;
    gap: 6px;
    color: var(--brand-green);
    font-weight: 700;
    letter-spacing: 0.04em;
    text-transform: uppercase;
    white-space: nowrap;
  }
  .brand-mark { background: var(--brand-green); flex: none; }
  .ghost-block { position: absolute; background: var(--ghost-green); }
  .web-band {
    position: absolute;
    background: var(--brand-green);
    color: #fff;
    font-size: 6px;
    letter-spacing: 0.2em;
    text-transform: uppercase;
    display: flex;
    align-items: center;
    justify-content: center;
    border-radius: 3px 3px 0 0;
    white-space: nowrap;
  }
  .base-rule { position: absolute; left: 0; right: 0; bottom: 0; height: 5px; background: var(--rule-dark); }

  /* Letterhead */
  .letterhead { left: 185px; top: 68px; width: 267px; height: 549px; }
  .letterhead .brand { position: absolute; top: 48px; left: 0; right: 0; justify-content: center; font-size: 11px; }
  .letterhead .brand-mark { width: 9px; height: 9px; }
  .letterhead .ghost-block { left: 72px; top: 190px; width: 124px; height: 124px; }
  .letterhead .contact-line {
    position: absolute; left: 14px; right: 14px; bottom: 27px;
    display: flex; justify-content: space-between;
    font-size: 3.8px; color: var(--ink-soft); white-space: nowrap;
  }
  .contact-line span { display: flex; align-items: center; gap: 2px; }
  .contact-line svg { width: 5px; height: 5px; fill: var(--brand-green); }
  .letterhead .web-band { right: 14px; bottom: 5px; width: 145px; height: 12px; font-size: 5px; }

  /* Folder */
  .folder { left: 637px; top: 46px; width: 345px; height: 571px; }
  .folder .brand { position: absolute; top: 268px; left: 0; right: 0; justify-content: center; font-size: 17px; gap: 7px; }
  .folder .brand-mark { width: 14px; height: 14px; }
  .folder .web-band { right: 24px; bottom: 5px; width: 200px; height: 14px; font-size: 6px; }

  /* Business cards */
  .card { left: 41px; width: 137px; height: 91px; }
  .card-front { top: 655px; }
  .card-front .brand { position: absolute; top: 16px; left: 0; right: 0; justify-content: center; font-size: 7px; gap: 4px; }
  .card-front .brand-mark { width: 6px; height: 6px; }
  .card-front .details { position: absolute; left: 0; right: 0; top: 36px; text-align: center; font-size: 4.2px; line-height: 1.6; color: var(--ink-soft); }
  .card-front .details .person { color: var(--ink); font-weight: 700; }
  .card-back { top: 779px; background: linear-gradient(135deg, var(--brand-green), var(--brand-green-dark)); border-color: var(--brand-green-dark); }
  .card-back .details { position: absolute; left: 0; right: 0; top: 30px; text-align: center; font-size: 4.6px; line-height: 1.8; color: #fff; }

  /* Envelope front */
  .envelope-front { left: 264px; top: 667px; width: 335px; height: 221px; }
  .envelope-front .brand { position: absolute; top: 20px; left: 40px; font-size: 9px; gap: 5px; }
  .envelope-front .brand-mark { width: 8px; height: 8px; }
  .envelope-front .return-address { position: absolute; left: 40px; top: 42px; font-size: 4.2px; line-height: 1.6; color: var(--ink-soft); }
  .envelope-front .ghost-block { left: 208px; top: 66px; width: 112px; height: 112px; }
  .envelope-front .web-band { left: 117px; bottom: 5px; width: 198px; height: 12px; font-size: 5.5px; }

  /* Envelope back */
  .envelope-back { left: 736px; top: 667px; width: 363px; height: 221px; }
  .envelope-back svg { position: absolute; left: 0; top: 0; }
  .envelope-back .flap-web {
    position: absolute; top: 34px; left: 0; right: 0; text-align: center;
    font-size: 5.5px; letter-spacing: 0.2em; text-transform: uppercase; color: #fff;
  }
</style>
</head>
<body>

<section class="sheet letterhead" aria-label="Letterhead">
  <div class="brand"><span class="brand-mark"></span>Bramblecourt Homes</div>
  <div class="ghost-block"></div>
  <div class="contact-line">
    <span><svg viewBox="0 0 10 10"><path d="M2 1h2l1 3-1.5 1a6 6 0 0 0 2.5 2.5L7 6l3 1v2c0 .6-.4 1-1 1A8 8 0 0 1 1 2c0-.6.4-1 1-1z"/></svg>+1 202 555 0147</span>
    <span><svg viewBox="0 0 10 10"><path d="M5 0a3.5 3.5 0 0 0-3.5 3.5C1.5 6 5 10 5 10s3.5-4 3.5-6.5A3.5 3.5 0 0 0 5 0zm0 5a1.5 1.5 0 1 1 0-3 1.5 1.5 0 0 1 0 3z"/></svg>4817 Larkspur Ave Suite 210, Washington, DC</span>
    <span><svg viewBox="0 0 10 10"><path d="M0 2h10v6H0z"/></svg>dgpelletier@bramblecourthomes.net</span>
  </div>
  <div class="web-band">www.bramblecourthomes.net</div>
  <div class="base-rule"></div>
</section>

<section class="sheet folder" aria-label="Presentation folder">
  <div class="brand"><span class="brand-mark"></span>Bramblecourt Homes</div>
  <div class="web-band">www.bramblecourthomes.net</div>
  <div class="base-rule"></div>
</section>

<section class="sheet card card-front" aria-label="Business card front">
  <div class="brand"><span class="brand-mark"></span>Bramblecourt Homes</div>
  <div class="details">
    <div class="person">Dorian Pelletier</div>
    <div>Managing Member</div>
    <div>4817 Larkspur Ave Suite 210, Washington, DC</div>
    <div>dgpelletier@bramblecourthomes.net</div>
    <div>Business License # 782645113058</div>
  </div>
</section>

<section class="sheet card card-back" aria-label="Business card back">
  <div class="details">
    <div>Cash Buyer, Fast Closing.</div>
    <div>Residential and Commercial</div>
    <div>We are a Nation Wide Buyer.</div>
  </div>
</section>

<section class="sheet envelope-front" aria-label="Envelope front">
  <div class="brand"><span class="brand-mark"></span>Bramblecourt Homes</div>
  <div class="return-address">
    <div>4817 Larkspur Ave Suite 210</div>
    <div>Washington, DC</div>
  </div>
  <div class="ghost-block"></div>
  <div class="web-band">www.bramblecourthomes.net</div>
  <div class="base-rule"></div>
</section>

<section class="sheet envelope-back" aria-label="Envelope back">
  <svg width="363" height="221" viewBox="0 0 363 221">
    <defs>
      <linearGradient id="flapGreen" x1="0" y1="0" x2="0" y2="1">
        <stop offset="0" stop-color="#1f9a4a"/>
        <stop offset="1" stop-color="#0f7434"/>
      </linearGradient>
    </defs>
    <path d="M0 0H363V18L198 74Q181.5 80 165 74L0 18Z" fill="url(#flapGreen)"/>
  </svg>
  <div class="flap-web">www.bramblecourthomes.net</div>
</section>

</body>
</html>
```